Church business card and letterhead
Delaware
Modern
Tessa Brindley
Leader of Family Ministry
58 North Quarry Lane
Delaware OH 43015
homecare@plainsnet.vormiq.com
gravhollow.org
Also need letterhead. You can use same info for letterhead; we will adjust at time of print. Idris at markforge has the logo.
logo design. we will also need the designers to create the vector file for this logo when they deliver the final files.
Any designer not willing to do that should not submit designs.

```html
<!DOCTYPE html>
<html lang="en">
<head>
<meta charset="utf-8">
<title>Gravhollow Chapel Stationery</title>
<link href="https://fonts.googleapis.com/css2?family=Lato:wght@400;700&display=swap" rel="stylesheet">
<style>
  :root {
    --backdrop: #e6e7ea;
    --paper: #ffffff;
    --purple: #7a2d8c;
    --purple-soft: #e9dcef;
    --ink: #4a4a52;
    --rule: #c9c2d0;
    --shadow: 0 3px 10px rgba(0,0,0,0.18);
  }
  * { box-sizing: border-box; margin: 0; padding: 0; }
  html, body { width: 1200px; height: 614px; overflow: hidden; }
  body {
    background: var(--backdrop);
    font-family: "Lato", sans-serif;
    color: var(--ink);
    position: relative;
  }
  .piece { position: absolute; background: var(--paper); box-shadow: var(--shadow); overflow: hidden; }

  .brand { display: flex; align-items: center; gap: 6px; }
  .brand-dot { width: 14px; height: 14px; border-radius: 50%; background: var(--purple); flex: none; }
  .brand-name { font-weight: 700; color: var(--purple); font-size: 12px; line-height: 1.05; }

  .faint-mark {
    position: absolute; border-radius: 50%;
    background: radial-gradient(circle, var(--purple-soft) 0%, rgba(233,220,239,0.25) 70%, rgba(233,220,239,0) 100%);
  }

  /* Envelope */
  .envelope { left: 40px; top: 130px; width: 300px; height: 140px; }
  .envelope .brand { position: absolute; left: 14px; top: 14px; }
  .envelope .return { position: absolute; left: 34px; top: 46px; font-size: 7px; line-height: 1.4; }

  /* Card back */
  .card-back { left: 55px; top: 300px; width: 250px; height: 135px; background: var(--purple); }
  .card-back .brand { position: absolute; left: 50%; top: 44px; transform: translateX(-50%); }
  .card-back .brand-dot { background: #fff; }
  .card-back .brand-name { color: #fff; font-size: 14px; }
  .card-back .web { position: absolute; width: 100%; bottom: 26px; text-align: center; color: #fff; font-size: 8px; letter-spacing: 1px; }

  /* Card front */
  .card-front { left: 55px; top: 455px; width: 250px; height: 135px; }
  .card-front .brand { position: absolute; left: 12px; top: 12px; }
  .card-front .contact { position: absolute; left: 14px; top: 52px; font-size: 7px; line-height: 1.45; }
  .card-front .person { position: absolute; right: 14px; bottom: 20px; text-align: right; }
  .person-name { font-weight: 700; color: var(--purple); font-size: 10px; }
  .person-role { font-size: 7px; }
  .card-front .faint-mark { right: -20px; top: -10px; width: 110px; height: 110px; }

  /* Letterheads */
  .letterhead { top: 45px; width: 400px; height: 520px; }
  .letter-plain { left: 365px; }
  .letter-form { left: 785px; }
  .letterhead .brand { position: absolute; left: 26px; top: 24px; }
  .letterhead .brand-name { font-size: 13px; }
  .letter-address { position: absolute; right: 26px; top: 24px; font-size: 6.5px; line-height: 1.45; text-align: right; }
  .letterhead .faint-mark { left: 170px; top: 160px; width: 200px; height: 200px; }

  .form-title { position: absolute; right: 26px; top: 24px; font-size: 10px; font-weight: 700; color: var(--purple); }
  .care-table { position: absolute; left: 26px; top: 66px; width: 348px; border-collapse: collapse; font-size: 6.5px; }
  .care-table td { border: 1px solid var(--rule); height: 17px; padding: 0 4px; }
  .care-table .label { background: #f4eff7; width: 48px; }
  .checks { position: absolute; left: 26px; top: 148px; width: 348px; display: flex; justify-content: space-between; font-size: 6.5px; }
  .check { display: flex; align-items: center; gap: 3px; }
  .box { width: 7px; height: 7px; border: 1px solid var(--ink); }
</style>
</head>
<body>

<section class="piece envelope">
  <div class="brand"><span class="brand-dot"></span><span class="brand-name">Gravhollow<br>Chapel</span></div>
  <div class="return">58 North Quarry Lane<br>Delaware OH 43015</div>
</section>

<section class="piece card-back">
  <div class="brand"><span class="brand-dot"></span><span class="brand-name">Gravhollow Chapel</span></div>
  <div class="web">gravhollow.org</div>
</section>

<section class="piece card-front">
  <div class="faint-mark"></div>
  <div class="brand"><span class="brand-dot"></span><span class="brand-name">Gravhollow<br>Chapel</span></div>
  <div class="contact">
    58 North Quarry Lane<br>
    Delaware OH 43015<br>
    740 555 0148<br>
    homecare@plainsnet.vormiq.com<br>
    gravhollow.org
  </div>
  <div class="person">
    <div class="person-name">Tessa Brindley</div>
    <div class="person-role">Leader of Family Ministry</div>
  </div>
</section>

<section class="piece letterhead letter-plain">
  <div class="brand"><span class="brand-dot"></span><span class="brand-name">Gravhollow<br>Chapel</span></div>
  <div class="letter-address">58 North Quarry Lane<br>Delaware OH 43015<br>gravhollow.org</div>
  <div class="faint-mark"></div>
</section>

<section class="piece letterhead letter-form">
  <div class="brand"><span class="brand-dot"></span><span class="brand-name">Gravhollow<br>Chapel</span></div>
  <div class="form-title">Care Form</div>
  <table class="care-table">
    <tr><td class="label">Name</td><td></td><td class="label">Date</td><td></td></tr>
    <tr><td class="label">Phone</td><td></td><td class="label">Time</td><td></td></tr>
    <tr><td class="label">Address</td><td></td><td class="label">City</td><td></td></tr>
    <tr><td class="label">Email</td><td></td><td class="label">Notes</td><td></td></tr>
  </table>
  <div class="checks">
    <span class="check"><span class="box"></span>Prayer</span>
    <span class="check"><span class="box"></span>Home Visit</span>
    <span class="check"><span class="box"></span>Hospital Call</span>
    <span class="check"><span class="box"></span>Meal Delivery</span>
  </div>
  <div class="faint-mark"></div>
</section>

</body>
</html>
```